hi-tech exotic coatings company needs a business card

we need a business card design for a new company based in South Florida called BRV GROUP LLC. brv stands for "bonded resin veneering" we have a proprietary process to diffuse metallic elements from the periodic table of elements into and onto industrial or medical critical components ie gas turbine blades, prosthetic implants such as a prosthetic hip or chemical processing components .The end result is a coating or a diffusion of exotic alloys with exotic surface properties on our customers parts. BUT WE DON'T SELL COATINGS we enter into a joint venture or licence agreement if we solve the problem.We would like a slogan on the front ? something like " EXTENDING THE LIFE OR YOUR CRITICAL COMPONENTS" by itself or WITH SCIENCE or WITH TECHNOLOGY.or a better slogan.
Updates
slogan we would like to see on cards in small
Industry/Entity Type
Business

```html
<!DOCTYPE html>
<html lang="en">
<head>
<meta charset="utf-8">
<title>BRV Group LLC – Business Card</title>
<link rel="stylesheet" href="https://fonts.googleapis.com/css2?family=Didact+Gothic&family=Orbitron:wght@500&family=Open+Sans:wght@400&display=swap">
<style>
  :root {
    --stage: #e9e7e4;
    --card-white: #ffffff;
    --navy: #1f3a57;
    --blue-deep: #234a6e;
    --blue-mid: #4f86ab;
    --blue-light: #a9cbdc;
    --ink-light: #ffffff;
    --shadow: rgba(0, 0, 0, 0.28);
  }
  * { box-sizing: border-box; margin: 0; padding: 0; }
  html, body {
    width: 1200px;
    height: 1000px;
    overflow: hidden;
    background: var(--stage);
  }
  .stage {
    position: relative;
    width: 1200px;
    height: 1000px;
  }
  .card {
    position: absolute;
    width: 600px;
    height: 340px;
    box-shadow: 0 10px 28px var(--shadow);
    text-align: center;
  }
  .card--front {
    left: 70px;
    top: 110px;
    color: var(--ink-light);
    background:
      radial-gradient(circle at 77% 74%, rgba(255,255,255,0.85) 0, rgba(255,255,255,0.25) 4%, rgba(255,255,255,0) 10%),
      radial-gradient(circle at 70% 12%, rgba(255,255,255,0.6) 0, rgba(255,255,255,0) 6%),
      radial-gradient(ellipse at 10% 110%, var(--blue-light) 0, rgba(169,203,220,0) 55%),
      linear-gradient(160deg, var(--blue-mid) 0%, var(--blue-mid) 35%, var(--blue-deep) 100%);
  }
  .card--back {
    left: 530px;
    top: 540px;
    background: var(--card-white);
    color: var(--navy);
  }
  .rule {
    position: absolute;
    height: 1px;
  }
  .card--front .rule { background: var(--ink-light); left: 95px; width: 430px; }
  .card--front .rule--top { top: 72px; }
  .card--front .rule--bottom { top: 196px; }
  .card--back .rule { background: var(--navy); left: 160px; width: 300px; }
  .card--back .rule--top { top: 52px; }
  .card--back .rule--bottom { top: 140px; }

  .brand-mark {
    font-family: "Didact Gothic", sans-serif;
    letter-spacing: 10px;
    position: absolute;
    left: 0;
    right: 0;
  }
  .card--front .brand-mark { top: 82px; font-size: 56px; line-height: 64px; }
  .card--back .brand-mark { top: 58px; font-size: 42px; line-height: 48px; }

  .company-name {
    font-family: "Didact Gothic", sans-serif;
    position: absolute;
    left: 0;
    right: 0;
    text-transform: uppercase;
    word-spacing: -2px;
  }
  .card--front .company-name { top: 154px; font-size: 20px; letter-spacing: 0.5px; }
  .card--back .company-name { top: 112px; font-size: 14px; letter-spacing: 0.3px; }

  .slogan {
    font-family: "Didact Gothic", sans-serif;
    position: absolute;
    left: 50px;
    right: 30px;
    top: 248px;
    font-size: 19px;
    line-height: 24px;
  }

  .person-name {
    font-family: "Orbitron", sans-serif;
    font-weight: 500;
    position: absolute;
    left: 0; right: 0;
    top: 158px;
    font-size: 24px;
    letter-spacing: 2px;
    text-transform: uppercase;
  }
  .person-role {
    font-family: "Open Sans", sans-serif;
    position: absolute;
    left: 0; right: 0;
    top: 192px;
    font-size: 13px;
    letter-spacing: 0.5px;
    text-transform: uppercase;
  }
  .contact-list {
    font-family: "Open Sans", sans-serif;
    list-style: none;
    position: absolute;
    left: 0; right: 0;
    top: 232px;
    font-size: 14px;
    line-height: 19px;
  }
  .contact-list .label { margin-right: 6px; }
</style>
</head>
<body>
<main class="stage">
  <section class="card card--front" aria-label="Business card front">
    <div class="rule rule--top"></div>
    <div class="brand-mark">BRV</div>
    <div class="company-name">Bonded Resin Veneering Group LLC</div>
    <div class="rule rule--bottom"></div>
    <p class="slogan">Lasting Strength for Your Most Vital Components<br>through Research and Discovery</p>
  </section>

  <section class="card card--back" aria-label="Business card back">
    <div class="rule rule--top"></div>
    <div class="brand-mark">BRV</div>
    <div class="company-name">Bonded Resin Veneering Group LLC</div>
    <div class="rule rule--bottom"></div>
    <h1 class="person-name">Alex Rivera</h1>
    <p class="person-role">Position</p>
    <ul class="contact-list">
      <li><span class="label">p:</span>305.555.0142</li>
      <li><span class="label">m:</span>305.555.0187</li>
      <li><span class="label">e:</span>alex@brvgroupllc.com</li>
      <li>www.brvgroupllc.com</li>
    </ul>
  </section>
</main>
</body>
</html>
```